Plumbing Company After Business Card

Business card for a plumbing business that offers a variety of plumbing services including maintenance, domestic and commercial plumbing. My main focus is to offer high quality professional service. A logo on the card would be ideal. Any other questions feel free to email. Cheers

Looking for something modern and upmarket with preferably a matte black background

Business name is Crestline Plumbing and Gas

Industry/Entity Type

Plumbing

Contact Information for Business Card

Crestline Plumbing and Gas
Marcus Thorvale
0472519306
14 Karrabee Drive, Ascot 3550
crestlineplumbing@mailbay.com.au
ABN 64 915 207 338

Font styles to use
Sans Serif

Colors
1b1b1b
ffffff
3377b5

Requirements
Must have
• Domestic
• Commercial
• Maintenance

```html
<!DOCTYPE html>
<html lang="en">
<head>
<meta charset="utf-8">
<title>Crestline Plumbing and Gas — Business Card</title>
<link rel="stylesheet" href="https://fonts.googleapis.com/css2?family=Open+Sans:wght@300;400;600&display=swap">
<style>
  :root {
    --page-bg: #d9d6d2;
    --card-black: #1b1b1b;
    --card-edge: #141414;
    --emboss: #222222;
    --text-white: #ffffff;
    --text-soft: #c9c9c9;
    --text-muted: #8e8e8e;
    --accent-blue: #3377b5;
  }
  * { box-sizing: border-box; margin: 0; padding: 0; }
  html, body {
    width: 1200px;
    height: 784px;
    overflow: hidden;
    background: var(--page-bg);
    font-family: "Open Sans", Arial, sans-serif;
  }
  .sheet {
    width: 1200px;
    height: 784px;
    display: flex;
    align-items: center;
    justify-content: center;
    gap: 48px;
  }
  .card {
    position: relative;
    width: 540px;
    height: 330px;
    background: var(--card-black);
    border-radius: 4px;
    box-shadow: 0 10px 28px rgba(0,0,0,0.28);
    overflow: hidden;
  }

  /* Contact side */
  .card-contact .mark-block {
    position: absolute;
    left: -30px;
    top: -20px;
    width: 230px;
    height: 300px;
    background: var(--emboss);
    border-radius: 6px;
    box-shadow: inset 0 0 0 1px var(--card-edge);
  }
  .contact {
    position: absolute;
    left: 238px;
    top: 50px;
    color: var(--text-soft);
  }
  .contact-name {
    font-size: 14px;
    font-weight: 400;
    letter-spacing: 0.6px;
    text-transform: uppercase;
    margin-bottom: 14px;
    color: var(--text-soft);
  }
  .contact-line {
    display: flex;
    align-items: center;
    gap: 12px;
    margin-bottom: 10px;
    font-size: 12px;
    font-weight: 300;
  }
  .contact-line.phone { font-size: 15px; font-weight: 400; }
  .contact-icon {
    width: 18px;
    height: 18px;
    flex: none;
  }
  .contact-abn {
    padding-left: 30px;
    font-size: 11px;
    font-weight: 300;
    color: var(--text-muted);
  }

  /* Brand side */
  .brand {
    position: absolute;
    left: 0;
    right: 0;
    top: 104px;
    display: flex;
    flex-direction: column;
    align-items: center;
    gap: 14px;
  }
  .brand-square {
    width: 34px;
    height: 34px;
    background: var(--accent-blue);
  }
  .brand-name {
    font-size: 22px;
    font-weight: 600;
    letter-spacing: 0.4px;
    color: var(--text-white);
  }
  .services {
    position: absolute;
    left: 34px;
    right: 34px;
    bottom: 32px;
    display: flex;
    justify-content: space-between;
    list-style: none;
  }
  .service {
    font-size: 12px;
    font-weight: 400;
    letter-spacing: 3px;
    text-transform: uppercase;
    color: var(--text-muted);
  }
</style>
</head>
<body>
<main class="sheet">

  <section class="card card-contact" aria-label="Business card, contact side">
    <div class="mark-block" aria-hidden="true"></div>
    <div class="contact">
      <p class="contact-name">Marcus Thorvale</p>
      <p class="contact-line phone">
        <svg class="contact-icon" viewBox="0 0 18 18" aria-hidden="true">
          <circle cx="9" cy="9" r="8" fill="none" stroke="#c9c9c9" stroke-width="1"/>
          <path d="M6 5.2l1.6-.4 1 2.2-1 .8a5 5 0 0 0 2.6 2.6l.8-1 2.2 1-.4 1.6c-3.6.2-7-3.2-6.8-6.8z" fill="#c9c9c9"/>
        </svg>
        0472519306
      </p>
      <p class="contact-line">
        <svg class="contact-icon" viewBox="0 0 18 18" aria-hidden="true">
          <circle cx="9" cy="9" r="8" fill="none" stroke="#c9c9c9" stroke-width="1"/>
          <path d="M9 4.5a3 3 0 0 0-3 3c0 2.2 3 5.8 3 5.8s3-3.6 3-5.8a3 3 0 0 0-3-3z" fill="#c9c9c9"/>
          <circle cx="9" cy="7.5" r="1.1" fill="#1b1b1b"/>
        </svg>
        14 Karrabee Drive, Ascot 3550
      </p>
      <p class="contact-line">
        <svg class="contact-icon" viewBox="0 0 18 18" aria-hidden="true">
          <circle cx="9" cy="9" r="8" fill="none" stroke="#c9c9c9" stroke-width="1"/>
          <rect x="5" y="6" width="8" height="6" fill="#c9c9c9"/>
          <path d="M5 6l4 3.2L13 6" fill="none" stroke="#1b1b1b" stroke-width="0.9"/>
        </svg>
        crestlineplumbing@mailbay.com.au
      </p>
      <p class="contact-abn">ABN 64 915 207 338</p>
    </div>
  </section>

  <section class="card card-brand" aria-label="Business card, brand side">
    <div class="brand">
      <span class="brand-square" aria-hidden="true"></span>
      <h1 class="brand-name">Crestline Plumbing and Gas</h1>
    </div>
    <ul class="services">
      <li class="service">Domestic</li>
      <li class="service">Commercial</li>
      <li class="service">Maintenance</li>
    </ul>
  </section>

</main>
</body>
</html>
```